Dunmore Associates Banner Add

We are an international headhunting firm looking to target IT guys in Europe and USA to come and work in Singapore or Sydney (Australia). These guys will generally work in Trading firms / Banks / Top Tech Firms. Text - "Are you working in the Fin/ Tech space for a bank or High Frequency Trading firm as a technologist?We have your job in Singapore/ Sydney.Better / Great LifestyleWorking visa'sThe highest calibre clients.Bored with Brexit?Apply now.We need 5 pictures to rotate on a banner add to attract attention / represent this call to action.Some ideas… Guy on a laptop on a beach Sydney Skyline Singapore Skyline Bondi Beach Paradise beach picturesPeople playing on Beach London in the rain vs Sydney (sunny)Style needs to be classy, premium, well finished, boutique and in keeping with our website www.dunmore-associates-example.net. - hence any text you think could be worthwhile taking from there is fine.File formats: JPG, PNG, GIF Maximum file size: 3MB Media Sizes: Minimum: 600 × 315 pixels Recommended: 1200 × 628 pixels Image ratio: 1.91:1 To maximize advert delivery, Images need to be public property, no copyright. 5 rotating pictures incorporating the text, pictures and sell to create one banner add.

Target Market(s)

Banking/ Finance

Number of Pages Required

1 page

Requirements
Must have
• 5 different banners on rotate
Nice to have
• Classy, text suggested or snippets of as required, maybe black and white to match our logo's but injections of colour but full colour is also fine I could be converted.
Should not have
• not too flashy, should be elegant, classy pictures, clean like our website.
• www.dunmore-associates-example.net

```html
<!DOCTYPE html>
<html lang="en">
<head>
<meta charset="utf-8">
<title>Dunmore Associates – Rotating Banner Set</title>
<link rel="stylesheet" href="https://fonts.googleapis.com/css2?family=Alegreya+Sans:wght@400;700&family=Playfair+Display:ital,wght@0,400;0,900;1,900&display=swap">
<style>
  :root {
    --board: #e6e6e6;
    --ink-dark: #141215;
    --ink-black: #050505;
    --ink-teal: #04181a;
    --ink-night: #141416;
    --ink-charcoal: #121212;
    --text: #ffffff;
    --text-soft: #d9d9d9;
    --body-font: "Alegreya Sans", sans-serif;
    --display-font: "Playfair Display", serif;
  }
  * { box-sizing: border-box; margin: 0; padding: 0; }
  html, body { width: 1200px; height: 1200px; overflow: hidden; }
  body { background: var(--board); position: relative; font-family: var(--body-font); color: var(--text); }

  .banner {
    position: absolute; width: 526px; height: 275px; overflow: hidden;
    box-shadow: 0 10px 30px rgba(0,0,0,0.18);
  }
  .banner--parrot { left: 55px; top: 143px; background: var(--ink-dark); }
  .banner--cat { left: 55px; top: 462px; background: var(--ink-black); }
  .banner--pineapple { left: 55px; top: 781px; background: var(--ink-teal); }
  .banner--plane { left: 624px; top: 304px; background: var(--ink-night); }
  .banner--flowers { left: 624px; top: 622px; background: var(--ink-charcoal); }

  .photo { position: absolute; }

  .brand {
    position: absolute; font-family: var(--body-font); font-weight: 400;
    font-size: 7px; letter-spacing: 2.4px; line-height: 9.5px; text-transform: uppercase; color: var(--text);
    display: flex; align-items: center; gap: 5px;
  }
  .brand__dot { width: 9px; height: 9px; border: 1px solid var(--text); flex: none; }

  .pitch { position: absolute; font-size: 11.5px; line-height: 17.6px; color: var(--text-soft); }
  .pitch strong { font-weight: 700; color: var(--text); }
  .pitch__close { margin-top: 17px; }

  .headline { position: absolute; font-family: var(--display-font); font-weight: 400; font-size: 17.5px; line-height: 26px; color: var(--text); white-space: nowrap; }
  .headline__lead { font-weight: 900; }
  .headline__accent { font-weight: 900; font-style: italic; }
  .headline__second { padding-left: 51px; }

  .cta {
    position: absolute; width: 180px; height: 34px; border: 1px solid var(--text);
    font-size: 11.5px; display: flex; align-items: center; justify-content: center; color: var(--text); white-space: nowrap;
  }
  .cta strong { font-weight: 700; margin-left: 3px; }
</style>
</head>
<body>

<!-- Banner 1 -->
<section class="banner banner--parrot">
  <div class="photo" role="img" aria-label="Blue macaw perched on a branch" style="left:0;top:16px;width:130px;height:252px;background:radial-gradient(ellipse 30% 55% at 65% 50%, #1d3fb0 0%, #152c7a 45%, rgba(20,18,21,0) 100%);"></div>
  <div class="brand" style="left:152px;top:24px;"><span class="brand__dot"></span><span>Dunmore<br>Associates</span></div>
  <div class="pitch" style="left:267px;top:22px;">
    Are you working in <strong>the Tech space</strong><br>for a bank or High Frequency Trading firm<br>as a technologist?
    <p class="pitch__close">We have your job in Singapore.</p>
  </div>
  <div class="headline" style="left:168px;top:141px;">
    <div><span class="headline__lead">Great</span> Lifestyle. Working visa's.</div>
    <div class="headline__second">The <span class="headline__accent">highest calibre</span> clients.</div>
  </div>
  <div class="cta" style="left:267px;top:212px;">Bored with Brexit?<strong>Apply now</strong></div>
</section>

<!-- Banner 2 -->
<section class="banner banner--cat">
  <div class="photo" role="img" aria-label="Black cat with green eyes in shadow" style="left:0;top:0;width:330px;height:275px;background:radial-gradient(ellipse 55% 60% at 45% 50%, #222224 0%, #111112 55%, rgba(5,5,5,0) 100%);"></div>
  <div class="brand" style="left:21px;top:21px;"><span class="brand__dot"></span><span>Dunmore<br>Associates</span></div>
  <div class="pitch" style="left:306px;top:30px;">
    Are you <strong>working</strong> in the Fin space<br>for a bank as a technologist?
    <p class="pitch__close">We have your job <strong>in Sydney</strong>!</p>
  </div>
  <div class="headline" style="left:238px;top:147px;">
    <div><span class="headline__lead">Great</span> Lifestyle. Working visa's.</div>
    <div class="headline__second">The <span class="headline__accent">highest calibre</span> clients.</div>
  </div>
  <div class="cta" style="left:306px;top:212px;">Bored with Brexit?<strong>Apply now</strong></div>
</section>

<!-- Banner 3 -->
<section class="banner banner--pineapple">
  <div class="photo" role="img" aria-label="Golden pineapple on a dark pedestal" style="left:80px;top:56px;width:72px;height:219px;background:radial-gradient(ellipse 40% 30% at 50% 62%, #7a6420 0%, #3a3512 50%, rgba(4,24,26,0) 100%);"></div>
  <div class="brand" style="left:21px;top:21px;"><span class="brand__dot"></span><span>Dunmore<br>Associates</span></div>
  <div class="pitch" style="left:259px;top:22px;">
    Are you working in <strong>the Tech space</strong><br>for a bank or High Frequency Trading firm<br>as a technologist?
    <p class="pitch__close" style="margin-top:9px;">We have your job in Singapore.</p>
  </div>
  <div class="headline" style="left:233px;top:134px;">
    <div><span class="headline__lead">Great</span> Lifestyle. Working visa's.</div>
    <div class="headline__second">The <span class="headline__accent">highest calibre</span> clients.</div>
  </div>
  <div class="cta" style="left:259px;top:215px;">Bored with Brexit?<strong>Apply now</strong></div>
</section>

<!-- Banner 4 -->
<section class="banner banner--plane">
  <div class="photo" role="img" aria-label="Aircraft climbing with white contrails in a night sky" style="left:110px;top:124px;width:20px;height:151px;background:linear-gradient(to bottom, rgba(255,255,255,0.15), rgba(220,220,220,0.75));"></div>
  <div class="brand" style="left:21px;top:21px;"><span class="brand__dot"></span><span>Dunmore<br>Associates</span></div>
  <div class="pitch" style="left:287px;top:22px;">
    Are you <strong>working</strong> in the Fin space<br>for a bank as a technologist?
    <p class="pitch__close">We have your job <strong>in Sydney</strong>!</p>
  </div>
  <div class="headline" style="left:222px;top:140px;">
    <div><span class="headline__lead">Great</span> Lifestyle. Working visa's.</div>
    <div class="headline__second">The <span class="headline__accent">highest calibre</span> clients.</div>
  </div>
  <div class="cta" style="left:287px;top:212px;">Bored with Brexit?<strong>Apply now</strong></div>
</section>

<!-- Banner 5 -->
<section class="banner banner--flowers">
  <div class="photo" role="img" aria-label="Bouquet of pale pink chrysanthemums in low light" style="left:24px;top:56px;width:216px;height:184px;background:radial-gradient(ellipse 45% 45% at 65% 40%, #8a6a6a 0%, #3b3232 45%, rgba(18,18,18,0) 100%);"></div>
  <div class="brand" style="left:21px;top:21px;"><span class="brand__dot"></span><span>Dunmore<br>Associates</span></div>
  <div class="pitch" style="left:287px;top:22px;">
    Are you <strong>working</strong> in the Fin space<br>for a bank as a technologist?
    <p class="pitch__close">We have your job <strong>in Sydney</strong>!</p>
  </div>
  <div class="headline" style="left:244px;top:134px;">
    <div><span class="headline__lead">Great</span> Lifestyle. Working visa's.</div>
    <div class="headline__second">The <span class="headline__accent">highest calibre</span> clients.</div>
  </div>
  <div class="cta" style="left:287px;top:210px;">Bored with Brexit?<strong>Apply now</strong></div>
</section>

</body>
</html>
```